Roofing Company Realtor Marketing Flyer

We would like a design for marketing material aimed at realtors. We are seeking to build relationships with local realtors to ensure that both sellers and buyers are happy and confident with their roofing systems through roof inspections, Dry-Seal certification, roof repairs, and replacements if necessary.

There are three points that must be included:
1. Home inspectors are generalists. We are roof experts that specialize in diagnosing and fixing roofing problems.
2. We offer "Dry Seal" certification to offer peace of mind to homeowners.
3. We offer referral bonuses for realtors.

Target Market(s)

Realtors

Industry/Entity Type

Roofing

Font styles to use
Sans Serif

Colors

Designer to choose colors to be used in the design.

Requirements
Must have
• Must be double-sided.
• Must be similar to current marketing materials design. See website http://gablecrestmo.com and attached images for details.
• We would also like a "fanned out" version of our Sample Inspection Report showing glimpses of some of the images on the later pages (See attached documents).

```html
<!DOCTYPE html>
<html lang="en">
<head>
<meta charset="utf-8">
<title>Gable Crest – Dry-Seal Certification Flyer</title>
<link href="https://fonts.googleapis.com/css2?family=Open+Sans:wght@400;600&family=Roboto+Condensed:wght@400;700&display=swap" rel="stylesheet">
<style>
  :root {
    --orange: #f0831f;
    --orange-light: #f7a54a;
    --charcoal: #505051;
    --ink: #3f3f41;
    --white: #ffffff;
    --backdrop: #e8e8e8;
    --sky: #c9d1d6;
    --foliage: #48583a;
    --tile: #a8563a;
  }
  * { margin: 0; padding: 0; box-sizing: border-box; }
  html, body { width: 1200px; height: 665px; overflow: hidden; }
  body {
    background: var(--backdrop);
    font-family: "Open Sans", sans-serif;
    color: var(--ink);
  }
  .flyer {
    position: absolute;
    left: 365px;
    top: 0;
    width: 470px;
    height: 665px;
    overflow: hidden;
    background: var(--white);
  }
  .flyer-art { position: absolute; inset: 0; width: 470px; height: 665px; }
  .brand {
    position: absolute;
    top: 20px;
    left: 0;
    width: 100%;
    text-align: center;
    font-family: "Open Sans", sans-serif;
    font-weight: 600;
    font-size: 36px;
    letter-spacing: -0.5px;
    color: var(--orange);
  }
  .brand-mark {
    display: inline-block;
    width: 12px;
    height: 12px;
    background: var(--orange);
    margin-right: 8px;
    vertical-align: 6px;
  }
  .headline {
    position: absolute;
    right: 20px;
    top: 388px;
    text-align: right;
    font-family: "Roboto Condensed", sans-serif;
  }
  .headline-name {
    display: block;
    font-weight: 700;
    font-size: 31px;
    line-height: 1;
    color: var(--charcoal);
  }
  .headline-title {
    display: block;
    font-weight: 700;
    font-size: 41px;
    line-height: 1.02;
    color: var(--orange);
  }
  .headline-sub {
    display: block;
    font-weight: 400;
    font-size: 15px;
    line-height: 1.2;
    color: var(--charcoal);
  }
  .benefits {
    position: absolute;
    left: 172px;
    right: 20px;
    top: 498px;
    list-style: none;
    font-size: 11.2px;
    line-height: 1.32;
    color: var(--ink);
  }
  .benefits li {
    position: relative;
    padding-left: 14px;
    margin-bottom: 5px;
    text-align: justify;
  }
  .benefits li::before {
    content: "";
    position: absolute;
    left: 0;
    top: 3px;
    width: 8px;
    height: 8px;
    background: var(--orange);
  }
  .contact {
    position: absolute;
    left: 170px;
    right: 10px;
    top: 606px;
    text-align: center;
    color: var(--white);
    font-size: 9.5px;
    line-height: 1.4;
  }
  .contact-rule { display: block; margin: 0 auto 6px; }
  .contact-sep { margin: 0 6px; }
</style>
</head>
<body>
  <article class="flyer">
    <svg class="flyer-art" viewBox="0 0 470 665" aria-hidden="false">
      <defs>
        <linearGradient id="footer-fade" x1="0" y1="0" x2="0" y2="1">
          <stop offset="0" stop-color="#ffffff"/>
          <stop offset="0.62" stop-color="#ffffff"/>
          <stop offset="0.82" stop-color="#f9c48e"/>
          <stop offset="1" stop-color="#f0831f"/>
        </linearGradient>
        <linearGradient id="photo-tones" x1="0" y1="0" x2="0.4" y2="1">
          <stop offset="0" stop-color="#f4f5f6"/>
          <stop offset="0.22" stop-color="#c9d1d6"/>
          <stop offset="0.42" stop-color="#4f5d3f"/>
          <stop offset="0.7" stop-color="#7a5446"/>
          <stop offset="1" stop-color="#a8563a"/>
        </linearGradient>
        <linearGradient id="swoosh-orange" x1="0" y1="1" x2="1" y2="0">
          <stop offset="0" stop-color="#f0831f"/>
          <stop offset="1" stop-color="#f39a3a"/>
        </linearGradient>
      </defs>

      <rect class="page-ground" width="470" height="665" fill="url(#footer-fade)"/>

      <path class="hero-photo" role="img" aria-label="Photo of a roofer in a safety harness climbing a tiled roof, trees and a yellow crane behind"
            d="M0,0 H470 V150 C330,215 210,330 150,470 L70,560 L0,400 Z" fill="url(#photo-tones)"/>
      <rect width="470" height="95" fill="#ffffff" opacity="0.55"/>

      <path class="band-charcoal" d="M470,108 C360,150 250,260 172,430 L196,432 C280,300 380,228 470,212 Z" fill="var(--charcoal)"/>
      <path class="band-orange" d="M0,392 L68,560 C140,390 290,225 470,160 L470,186 C330,240 200,365 104,560 L92,585 Z" fill="url(#swoosh-orange)"/>
      <path class="band-orange-tail" d="M0,392 L92,585 L104,560 L68,560 Z" fill="var(--orange)"/>
      <path d="M0,392 L68,560 C140,390 290,225 470,160" fill="none" stroke="#ffffff" stroke-width="5"/>
      <path d="M104,560 C200,365 330,240 470,186" fill="none" stroke="#ffffff" stroke-width="5"/>
      <path class="corner-charcoal" d="M0,452 L80,620 L0,665 Z" fill="var(--charcoal)"/>
      <path d="M0,452 L80,620" fill="none" stroke="#ffffff" stroke-width="5"/>
    </svg>

    <div class="brand"><span class="brand-mark"></span>Gable Crest</div>

    <h1 class="headline">
      <span class="headline-name">Dry-Seal</span>
      <span class="headline-title">Certification</span>
      <span class="headline-sub">Roof Repairs &amp; Replacements</span>
    </h1>

    <ul class="benefits">
      <li>Home inspectors are generalists. We are roof experts that specialize in diagnosing and fixing roofing problems.</li>
      <li>We offer "Dry Seal" certification to offer peace of mind to homeowners.</li>
      <li>We offer referral bonuses for realtors.</li>
    </ul>

    <footer class="contact">
      <svg class="contact-rule" width="124" height="8" viewBox="0 0 124 8" aria-hidden="true">
        <line x1="4" y1="4" x2="120" y2="4" stroke="#ffffff" stroke-width="1.5"/>
        <rect x="0" y="0.5" width="7" height="7" fill="#ffffff"/>
        <rect x="58.5" y="0.5" width="7" height="7" fill="#ffffff"/>
        <rect x="117" y="0.5" width="7" height="7" fill="#ffffff"/>
      </svg>
      <div>844-GableCrest<span class="contact-sep">|</span>1870 Ridgeline Ave. Fenton, MO 63026</div>
      <div>www.gablecrestmo.com</div>
    </footer>
  </article>
</body>
</html>
```